BRIGHTWAVE PARTNERS NAMECARD

Need to design a name card with an existing logo.

As we are professional corporate services provider our name card has to project a professional image.
Should be corporate, simple & professional.

Our corporate color is maroon red but not too dull.

Please refer to our website at www.brightwavepartners.com.sg

Would attach our logo herewith.

Front surface of namecard details:
BRIGHTWAVE PARTNERS PTE LTD
Registration No. 208731945K

Lowe Hui Ting CA (Singapore)
Director

Tel +65 6481 2957
Mobile +65 9172 3806
lowe@brightwavepartners.com.sg
www.brightwavepartners.com.sg

47 Palmer Lane
#07-14 Harbourlight Plaza
Singapore 274153

Back of namecard:-
OUR CORE SERVICES
Incorporation services
Corporate Secretarial Services
Accountancy service
Goods & Services Taxation
Corporate & Personal Taxation
Financial Reporting
Payroll Administration

AFFILIATES:
TRIVANTA CORPORATE SERVICES PTE LTD
BRIGHTWAVEREGISTRYPTE LTD
ORR MANAGEMENT SERVICES PTE LTD
DW LIM AND COMPANY PTE LTD
LEDGERWISE ACADEMY

```html
<!DOCTYPE html>
<html lang="en">
<head>
<meta charset="utf-8">
<title>Brightwave Partners Name Card</title>
<link rel="stylesheet" href="https://fonts.googleapis.com/css2?family=Marcellus&family=Roboto:wght@400;500&display=swap">
<style>
  :root {
    --brand-red: #d11f30;
    --card-white: #ffffff;
    --ink: #1d1d1d;
    --backdrop: #5d666c;
    --backdrop-light: #7a8388;
  }
  * { box-sizing: border-box; margin: 0; padding: 0; }
  html, body { width: 1200px; height: 900px; overflow: hidden; }
  body {
    background: radial-gradient(ellipse at 50% 40%, var(--backdrop-light), var(--backdrop));
    position: relative;
    font-family: "Roboto", Arial, sans-serif;
  }
  .card {
    position: absolute;
    top: 294px;
    width: 520px;
    height: 312px;
    border-radius: 18px;
    box-shadow: 0 10px 24px rgba(0,0,0,0.35);
    overflow: hidden;
  }
  .card--back { left: 60px; background: var(--brand-red); color: var(--card-white); font-family: "Marcellus", Georgia, serif; }
  .card--front { left: 620px; background: var(--card-white); color: var(--ink); }

  .brand-name {
    position: absolute;
    display: flex;
    align-items: center;
    gap: 10px;
    font-family: "Roboto", Arial, sans-serif;
    font-weight: 500;
    white-space: nowrap;
    letter-spacing: 0.5px;
  }
  .brand-name__mark { width: 0.7em; height: 0.7em; background: currentColor; flex: none; }
  .card--back .brand-name { left: 150px; top: 78px; font-size: 28px; color: var(--card-white); }
  .card--front .brand-name { left: 34px; top: 42px; font-size: 22px; color: var(--brand-red); }

  .label {
    display: inline-block;
    background: var(--card-white);
    color: var(--brand-red);
    font-size: 10px;
    padding: 3px 7px;
    letter-spacing: 0.3px;
  }
  .services { position: absolute; left: 28px; top: 146px; }
  .services ul { list-style: none; margin-top: 7px; font-size: 10.5px; line-height: 1.4; }
  .affiliates { position: absolute; right: 26px; bottom: 32px; display: flex; align-items: flex-start; gap: 10px; }
  .affiliates ul { list-style: none; text-align: right; font-size: 10.5px; line-height: 1.4; letter-spacing: 0.3px; }

  .person { position: absolute; left: 34px; top: 102px; }
  .person__name { color: var(--brand-red); font-size: 13px; }
  .person__name small { font-size: 9px; }
  .person__role { font-size: 8px; margin-top: 1px; }
  .divider { position: absolute; left: 34px; right: 28px; top: 138px; height: 1.5px; background: var(--brand-red); }
  .registration { position: absolute; right: 28px; top: 122px; font-size: 10.5px; }
  .contacts { position: absolute; left: 34px; top: 152px; list-style: none; font-size: 10.5px; line-height: 1.75; }
  .contacts li { display: flex; align-items: center; gap: 8px; }
  .contacts svg { width: 10px; height: 10px; flex: none; }
  .address { position: absolute; right: 28px; top: 150px; font-size: 10.5px; line-height: 1.4; text-align: left; }
</style>
</head>
<body>

<section class="card card--back" aria-label="Card back">
  <div class="brand-name"><span class="brand-name__mark"></span>BRIGHTWAVE PARTNERS</div>
  <div class="services">
    <span class="label">OUR CORE SERVICES</span>
    <ul>
      <li>Incorporation services</li>
      <li>Corporate Secretarial Services</li>
      <li>Accountancy service</li>
      <li>Goods &amp; Services Taxation</li>
      <li>Corporate &amp; Personal Taxation</li>
      <li>Financial Reporting</li>
      <li>Payroll Administration</li>
    </ul>
  </div>
  <div class="affiliates">
    <ul>
      <li>TRIVANTA CORPORATE SERVICES PTE LTD</li>
      <li>BRIGHTWAVEREGISTRYPTE LTD</li>
      <li>ORR MANAGEMENT SERVICES PTE LTD</li>
      <li>DW LIM AND COMPANY PTE LTD</li>
      <li>LEDGERWISE ACADEMY</li>
    </ul>
    <span class="label">AFFILIATES</span>
  </div>
</section>

<section class="card card--front" aria-label="Card front">
  <div class="brand-name"><span class="brand-name__mark"></span>BRIGHTWAVE PARTNERS</div>
  <div class="person">
    <div class="person__name">Lowe Hui Ting CA <small>(Singapore)</small></div>
    <div class="person__role">Director</div>
  </div>
  <div class="registration">Registration No. 208731945K</div>
  <div class="divider"></div>
  <ul class="contacts">
    <li><svg viewBox="0 0 10 10"><path d="M2 1l2 2-1 1.2c.6 1.2 1.5 2.1 2.8 2.8L7 6l2 2-1.3 1.3C4.5 9 1 5.5.7 2.3z" fill="var(--brand-red)"/></svg>+65 6481 2957</li>
    <li><svg viewBox="0 0 10 10"><rect x="2.5" y="0.5" width="5" height="9" rx="1" fill="none" stroke="var(--brand-red)"/><circle cx="5" cy="8" r=".6" fill="var(--brand-red)"/></svg>+65 9172 3806</li>
    <li><svg viewBox="0 0 10 10"><rect x="0.5" y="2" width="9" height="6" fill="var(--brand-red)"/><path d="M.5 2L5 5.5 9.5 2" fill="none" stroke="#fff" stroke-width=".8"/></svg>lowe@brightwavepartners.com.sg</li>
    <li><svg viewBox="0 0 10 10"><circle cx="5" cy="5" r="4.5" fill="var(--brand-red)"/><path d="M.5 5h9M5 .5c-2 2.5-2 6.5 0 9M5 .5c2 2.5 2 6.5 0 9" fill="none" stroke="#fff" stroke-width=".6"/></svg>www.brightwavepartners.com.sg</li>
  </ul>
  <div class="address">47 Palmer Lane<br>#07-14 Harbourlight Plaza<br>Singapore 274153</div>
</section>

</body>
</html>
```